Reggie Dunmore Personalised Health, Performance and Longevity Exec Coach

Business Card for www.reggiedunmore.net site. It is a trust site and I use it for 1:1 relatable connections. It is the one I use for building intimate 1:1 trust building and Exec Coaching Services and programs for high wealth individuals and corporates. I also have a commercial programmatic site of my personal health products and services and programs for main stream one to many. www.reggiedunmore.net that can also provoke thought for the www.reggiedunmore.net business card. (mind you will get a separate business card for that site, but want to provide context). It has a logo which you may want to draw from in designing the reggiedunmore business card which is personal and is about building my brand. There is also a reggiedunmore personal QV page and reggiedunmore business QV page. I am a Certified Talent Compass 3.1 Coach with Norvane and you can get a corporate brief of me on there to give you more context https://www.norvanetalenthub.com/coach/en-us/directory?search=reggie

Target Market(s)

Being a Personalised Health Coach I am focused on Health>Performance>Longevity>Wellbeing. Target market is Executives /High Wealth individuals/Corporates. I am most relatable to the IT industry as I was ion it building partnerships for IT companies for 28+ years.

Industry/Entity Type

Health And Wellness

Contact Information for Business Card

Name: Reggie Dunmore
email: reggie@reggiedunmore.net
Phone: Australia +61 408316924 Singapore +65 93402871

Font styles to use
Sans Serif
Other font styles liked:
• Arial and Calibra could work?

Colors

Designer to choose colors to be used in the design.

Requirements
Must have
• It must be a no BS design that is intimate. In keeping with the reggiedunmore.net website I'm guessing grey scale. It may be printed on plastic as well for durability and a point of difference. It must have people feeling trust and feeling safe to be 1:1 personal. It's about helping people move from stuck to sustainable change. Moving them to a healthier state, increasing performance if and where they want, longevity and well being.
Nice to have
• On the back you can place a logo that is in line with what I have as a colourful mandala at www.reggiedunmore.net. It will be on the landing page and top left of each page in that site. A greyscale simpler version to create linkage to my philosophy. Also you could have the continuum of Personalised Health > > Performance > Longevity > Wellbeing as well or instead of in your designs some how infographcially represented if not using the existing logo at Fortysomethingrevival.com
Should not have
• Clutter is a no no. Keep it clean, easy to read, no BS feel. Must be authentic and warm yet smart.

```html
<!DOCTYPE html>
<html lang="en">
<head>
<meta charset="utf-8">
<title>Reggie Dunmore – Business Card</title>
<link rel="stylesheet" href="https://fonts.googleapis.com/css2?family=Montserrat:ital,wght@0,500;0,600;1,700&family=Arimo:wght@700&family=Caveat:wght@400&display=swap">
<style>
  :root {
    --backdrop: #000000;
    --card: #ffffff;
    --ink: #555659;
    --ink-dark: #1c1c1c;
    --rule: #b9b9b9;
    --health: #00a8e6;
    --performance: #2d3891;
    --longevity: #f8a51f;
    --wellbeing: #7fc241;
    --on-colour: #ffffff;
  }
  * { box-sizing: border-box; margin: 0; padding: 0; }
  html, body { width: 1129px; height: 1200px; overflow: hidden; background: var(--backdrop); }
  .canvas { position: relative; width: 1129px; height: 1200px; }

  .card { position: absolute; left: 136px; width: 856px; height: 490px; background: var(--card); overflow: hidden; }
  .card--front { top: 74px; }
  .card--back { top: 638px; }

  .portrait {
    position: absolute; left: 44px; top: 94px; width: 268px; height: 384px;
    background: radial-gradient(ellipse 60% 55% at 50% 45%, #3a3a3a 0%, #6a6a6a 50%, #d8d8d8 80%, #ffffff 100%);
  }

  .tagline {
    position: absolute; right: 222px; top: 88px;
    font: italic 700 23px/1 "Montserrat", sans-serif; color: var(--ink);
  }
  .tagline-rule { position: absolute; left: 382px; top: 120px; width: 252px; height: 2px; background: var(--rule); }

  .brand-mark { position: absolute; left: 664px; top: 30px; width: 160px; height: 160px;
    display: flex; flex-direction: column; align-items: center; justify-content: center; gap: 8px; }
  .brand-mark__dot { width: 54px; height: 54px; border-radius: 50%; background: var(--wellbeing); }
  .brand-mark__name { font: 600 14px/1.2 "Montserrat", sans-serif; color: var(--ink); text-align: center; }

  .name {
    position: absolute; left: 354px; top: 210px;
    font: 400 54px/1 "Caveat", cursive; color: var(--ink-dark); letter-spacing: 1px;
  }

  .contacts { position: absolute; left: 352px; top: 290px; list-style: none; }
  .contacts li { position: relative; height: 40.5px; padding-left: 32px;
    font: 500 19px/22px "Montserrat", sans-serif; color: var(--ink); letter-spacing: .2px; white-space: nowrap; }
  .contacts svg { position: absolute; left: 0; top: 1px; width: 20px; height: 20px; fill: var(--ink); }

  .continuum { position: absolute; left: 0; top: 133px; width: 856px; height: 224px; display: flex; gap: 3px; }
  .stage { position: relative; flex: 1; display: flex; flex-direction: column; align-items: center; color: var(--on-colour); }
  .stage--health { background: var(--health); }
  .stage--performance { background: var(--performance); }
  .stage--longevity { background: var(--longevity); }
  .stage--wellbeing { background: var(--wellbeing); }
  .stage__icon { position: absolute; top: 38px; width: 68px; height: 68px; }
  .stage__label { position: absolute; top: 128px; width: 100%; text-align: center;
    font: 700 20px/30px "Arimo", Arial, sans-serif; letter-spacing: .3px; }
  .stage__label--single { top: 143px; }
  .stage__chevron { position: absolute; left: -14px; top: 64px; width: 40px; height: 96px; opacity: .28; }
</style>
</head>
<body>
<main class="canvas">

  <section class="card card--front">
    <div class="portrait" role="img" aria-label="Black and white portrait photo of Reggie Dunmore, arms crossed, dark t-shirt"></div>

    <p class="tagline">Optimising Life</p>
    <div class="tagline-rule"></div>

    <div class="brand-mark">
      <span class="brand-mark__dot"></span>
      <span class="brand-mark__name">Fortysomething Revival</span>
    </div>

    <h1 class="name">Reggie Dunmore</h1>

    <ul class="contacts">
      <li><svg viewBox="0 0 24 24"><path d="M6.6 2.5l3 3.4-1.9 2.6c1.2 2.8 3.4 5.1 6.2 6.4l2.6-1.9 3.5 3-1.6 3.4c-8.6-.4-15.2-7.2-15.6-15.6z"/></svg>AUSTRALIA: +61 408 316 924</li>
      <li>SINGAPORE: +65 9340 2871</li>
      <li><svg viewBox="0 0 24 24"><path d="M2 5h20l-10 7.5z"/><path d="M2 7.5l10 7.5 10-7.5V19H2z"/></svg>REGGIE@REGGIEDUNMORE.NET</li>
      <li><svg viewBox="0 0 24 24"><circle cx="12" cy="12" r="10"/><path d="M7 6c2 1 3 3 2 5s1 3 0 5M14 4c-1 2 1 3 3 3s2 3 1 5-2 2-3 5" stroke="#fff" stroke-width="1.6" fill="none"/></svg>WWW.REGGIEDUNMORE.NET</li>
    </ul>
  </section>

  <section class="card card--back">
    <div class="continuum">
      <div class="stage stage--health">
        <svg class="stage__icon" viewBox="0 0 68 68" fill="#fff">
          <path d="M34 40C24 32 20 28 20 22a7 7 0 0 1 14-2 7 7 0 0 1 14 2c0 6-4 10-14 18z"/>
          <path d="M4 24c2 8 8 14 14 18l4 14h8V46c0-4-4-8-10-12l-6-6c-2-6-8-8-10-4z"/>
          <path d="M64 24c-2 8-8 14-14 18l-4 14h-8V46c0-4 4-8 10-12l6-6c2-6 8-8 10-4z"/>
        </svg>
        <p class="stage__label">PERSONALISED<br>HEALTH</p>
      </div>
      <div class="stage stage--performance">
        <svg class="stage__chevron" viewBox="0 0 40 96"><path d="M0 0h18l22 48-22 48H0l22-48z" fill="#fff"/></svg>
        <svg class="stage__icon" viewBox="0 0 68 68">
          <circle cx="34" cy="34" r="33" fill="#fff"/>
          <path d="M12 54l14-20 4 10 14-22" fill="none" stroke="#2d3891" stroke-width="5" stroke-linejoin="miter"/>
          <path d="M38 16l14-4-2 14z" fill="#2d3891"/>
        </svg>
        <p class="stage__label stage__label--single">PERFORMANCE</p>
      </div>
      <div class="stage stage--longevity">
        <svg class="stage__chevron" viewBox="0 0 40 96"><path d="M0 0h18l22 48-22 48H0l22-48z" fill="#fff"/></svg>
        <svg class="stage__icon" viewBox="0 0 68 68">
          <path d="M52 12A31 31 0 1 0 62 30" fill="none" stroke="#fff" stroke-width="4"/>
          <path d="M46 6l14 2-6 12z" fill="#fff"/>
          <path d="M24 20l12 16" stroke="#fff" stroke-width="5" stroke-linecap="round"/>
        </svg>
        <p class="stage__label stage__label--single">LONGEVITY</p>
      </div>
      <div class="stage stage--wellbeing">
        <svg class="stage__chevron" viewBox="0 0 40 96"><path d="M0 0h18l22 48-22 48H0l22-48z" fill="#fff"/></svg>
        <svg class="stage__icon" viewBox="0 0 68 68">
          <circle cx="34" cy="34" r="33" fill="#fff"/>
          <circle cx="34" cy="18" r="5" fill="#7fc241"/>
          <path d="M20 14l10 12v24h3V38h2v12h3V26l10-12" fill="none" stroke="#7fc241" stroke-width="4" stroke-linejoin="round"/>
        </svg>
        <p class="stage__label stage__label--single">WELLBEING</p>
      </div>
    </div>
  </section>

</main>
</body>
</html>
```